Kettle Ledger Business Card design

We need a stand out business card design for Accounting practice based in Australia specialising in pubs, clubs and hotels. We help venues maximise margins, create time and manage cashflow. One club we have been working with for the last 6 months has increased revenue by 3% and margin by 5% in this time frame. We have a back office outsourced system that costs less than having a full time employee and also allows the venues the added benefit of:<br/>-using the office space to become a revenue generating opportunity. <br/>-a complete system to enhance governance, accountability and efficiency within their operation<br/>-52 weeks cover so no hassle to cover annual/sick .. leave<br/><br/>We would like to see designs that use the colours of our logo (green & blue).
Target Market(s)
Australian Pubs, Clubs & Hotels abookkeeping, accounting and tax services
Industry/Entity Type
Accountant
Contact Information for Business Card
Miriam Oakley CPA
Principal
Accountant Tax Agent
Miriam@KettleLedger-example.com.au
0418693142
www.kettleledger-example.com.au
Accounting / Payroll / Tax / SMSF / Technology
Colors
Designer to choose colors to be used in the design.
Look and feel
Each slider illustrates characteristics of the customer's brand and the style your logo design should communicate.

```html
<!DOCTYPE html>
<html lang="en">
<head>
<meta charset="utf-8">
<title>Kettle Ledger Business Card</title>
<link rel="stylesheet" href="https://fonts.googleapis.com/css2?family=Montserrat:wght@700&family=Questrial&display=swap">
<style>
  :root {
    --brand-blue: #253f8f;
    --brand-green: #077040;
    --photo-light: #5fd19a;
    --photo-dark: #0b6b3e;
    --paper: #ffffff;
    --edge: #222222;
  }
  * { margin: 0; padding: 0; box-sizing: border-box; }
  html, body { width: 1200px; height: 1200px; overflow: hidden; background: var(--paper); }
  body { position: relative; font-family: "Questrial", sans-serif; }

  .card {
    position: absolute;
    left: 256px;
    width: 726px;
    height: 444px;
    border: 1px solid var(--edge);
    background: var(--paper);
    overflow: hidden;
  }
  .card--front { top: 116px; }
  .card--back { top: 647px; }

  .brand {
    position: absolute;
    top: 66px;
    left: 0;
    right: 0;
    display: flex;
    justify-content: center;
    align-items: center;
    gap: 16px;
  }
  .brand__dot {
    width: 46px;
    height: 46px;
    border-radius: 50%;
    border: 5px solid var(--brand-green);
  }
  .brand__name {
    font-family: "Montserrat", sans-serif;
    font-weight: 700;
    font-size: 50px;
    color: var(--brand-blue);
    letter-spacing: -0.5px;
  }

  .person {
    position: absolute;
    top: 178px;
    left: 0;
    right: 0;
    text-align: center;
  }
  .person__name {
    font-family: "Montserrat", sans-serif;
    font-weight: 700;
    font-size: 24px;
    color: var(--brand-blue);
  }
  .person__name .credential { font-family: "Questrial", sans-serif; font-weight: 400; font-style: italic; }
  .person__role {
    margin-top: 8px;
    font-size: 21px;
    line-height: 27px;
    color: var(--brand-green);
  }

  .contact {
    position: absolute;
    top: 286px;
    left: 0;
    right: 0;
    text-align: center;
    font-size: 18px;
    line-height: 24px;
    color: var(--brand-blue);
  }
  .contact__label { color: var(--brand-green); }

  .services {
    position: absolute;
    left: -1px;
    right: -1px;
    bottom: -1px;
    height: 67px;
    background: var(--brand-green);
    color: var(--paper);
    display: flex;
    align-items: center;
    justify-content: center;
    font-size: 25px;
    letter-spacing: 0.6px;
    word-spacing: 4px;
  }

  .venue-photo {
    position: absolute;
    top: 58px;
    left: -1px;
    right: -1px;
    height: 320px;
    background: linear-gradient(160deg, var(--photo-dark) 0%, #2fa56c 45%, var(--photo-light) 75%, var(--photo-dark) 100%);
  }

  .back-url {
    position: absolute;
    top: 390px;
    left: 0;
    right: 0;
    text-align: center;
    font-family: "Montserrat", sans-serif;
    font-weight: 700;
    font-size: 26px;
    color: var(--brand-green);
    letter-spacing: 0.3px;
  }
</style>
</head>
<body>
  <section class="card card--front">
    <div class="brand">
      <span class="brand__dot"></span>
      <span class="brand__name">Kettle Ledger</span>
    </div>

    <div class="person">
      <p class="person__name">Miriam Oakley <span class="credential">CPA</span></p>
      <p class="person__role">Principal<br>Accountant Tax Agent</p>
    </div>

    <div class="contact">
      <p><span class="contact__label">E:</span> Miriam@KettleLedger-example.com.au</p>
      <p><span class="contact__label">T:</span> 0418693142</p>
      <p><span class="contact__label">W:</span> www.kettleledger-example.com.au</p>
    </div>

    <div class="services">Accounting | Payroll | Tax | SMSF | Technology</div>
  </section>

  <section class="card card--back">
    <div class="venue-photo" role="img" aria-label="Green-tinted photograph of a pub interior with a bar, armchairs, potted trees and a checkered floor"></div>
    <p class="back-url">WWW.KETTLELEDGER-EXAMPLE.COM.AU</p>
  </section>
</body>
</html>
```